Lomi-Seret - Promote and Support a community

Design a website for Ethiopean Community. the design should be friendly, easy to navigate and maintain the look & feel of the Ethiopian culture. a proposed logo is attached but it can be change according to your recommendations. This is a project we are doing at a discount rate as it supports a weak community.
Please visit their current website http://www.lomi-seret.example.il/index.php?lang=en

Target Market(s)

Community members, potential doners

Industry/Entity Type

community

Number of Pages Required

1 page

Font styles to use
Sans Serif

Requirements
Must have
• easy to navigate friendly interface

```html
<!DOCTYPE html>
<html lang="en">
<head>
<meta charset="utf-8">
<title>Lomi-Seret – Promote and Support a Community</title>
<link href="https://fonts.googleapis.com/css2?family=Montserrat:wght@400;500;600;700;800&family=Oswald:wght@300;400&display=swap" rel="stylesheet">
<style>
:root{
  --red:#b3141c;
  --deep-red:#8e1419;
  --orange:#e7661c;
  --yellow:#f2d935;
  --gold:#f0c21a;
  --green:#0b7f3a;
  --teal:#0b6a48;
  --ink:#333;
  --muted:#666;
  --line:#e6b9bd;
  --white:#fff;
}
*{box-sizing:border-box;margin:0;padding:0}
html,body{width:1200px;height:4518px;overflow:hidden}
body{position:relative;background:var(--white);font-family:'Montserrat',sans-serif;color:var(--ink)}
.abs{position:absolute}
a{color:inherit;text-decoration:none}

/* header */
.site-header{left:0;top:0;width:1200px;height:93px;background:var(--white);z-index:5}
.brand{left:108px;top:18px;display:flex;align-items:center;gap:10px;font-weight:700;font-size:18px;color:var(--deep-red)}
.brand-dot{width:40px;height:40px;border-radius:50%;background:var(--red)}
.main-nav{left:287px;top:44px;display:flex;gap:0;font-size:12.5px;color:var(--red);letter-spacing:.2px}
.main-nav a{margin-right:41px}
.main-nav a.active{font-weight:700;border-bottom:2px solid var(--green);padding-bottom:6px}

/* hero */
.hero{left:0;top:93px;width:1200px;height:670px;clip-path:polygon(0 0,100% 0,100% 609px,0 100%);
  background:linear-gradient(100deg,#5b3a2a 0%,#a2704a 35%,#d9a46a 55%,#6e4a33 80%,#3b2518 100%)}
.hero-arrow{top:375px;width:24px;height:40px}
.hero-card{left:105px;top:268px;width:498px;height:251px;border-radius:40px 40px 0 0;
  background:linear-gradient(90deg,var(--gold) 0%,#ec8a18 45%,#d2261e 100%);padding:48px 0 0 50px}
.hero-card h1{font-weight:800;font-size:60px;color:var(--white);line-height:1;letter-spacing:1px}
.hero-card p{font-size:18px;font-weight:500;color:var(--white);margin:10px 0 0 8px}
.btn{display:inline-block;font-weight:700;text-transform:uppercase;text-align:center}
.btn-red{margin:18px 0 0 16px;width:160px;height:42px;line-height:42px;border-radius:20px 0 20px 0;background:var(--red);color:var(--white);font-size:13px}

/* about */
.about-frame{left:358px;top:819px;width:716px;height:437px;border:1px solid var(--line)}
.about-photo{left:106px;top:819px;width:438px;height:438px;border-radius:50%;border:12px solid var(--yellow);
  background:radial-gradient(circle at 50% 45%,#c98d66 0%,#8a5a44 50%,#6b7f70 100%)}
.eyebrow{font-family:'Oswald',sans-serif;font-weight:300;font-size:14px;letter-spacing:.5px}
.section-title{font-size:34px;font-weight:400;color:var(--deep-red);line-height:1}
.section-title b{font-weight:800}
.rule{width:44px;height:3px;background:var(--green)}
.about-eyebrow{left:586px;top:872px;color:var(--green)}
.about-title{left:584px;top:894px}
.about-rule{left:586px;top:938px}
.about-text{left:586px;top:966px;width:450px;font-size:13.2px;line-height:25px;color:#444}
.btn-green{background:var(--teal);color:var(--white);border-radius:20px 0 20px 0;font-size:14px}
.about-btn{left:577px;top:1138px;width:181px;height:50px;line-height:50px}

/* mission */
.mission{left:0;top:1307px;width:1200px;height:556px;clip-path:polygon(0 0,100% 61px,100% 494px,0 100%);
  background:linear-gradient(110deg,#7a0f17 0%,#b9161f 40%,#d7281c 70%,#e23a18 100%)}
.mission-eyebrow{left:0;top:1458px;width:1200px;text-align:center;color:var(--white);font-size:17px}
.mission-title{left:0;top:1484px;width:1200px;text-align:center;color:var(--white);font-size:37px}
.mission-rule{left:580px;top:1530px;background:var(--yellow)}
.mission-text{left:260px;top:1548px;width:680px;text-align:center;color:var(--white);font-size:15.5px;line-height:24px}
.btn-yellow{background:var(--yellow);color:var(--red);border-radius:20px 0 20px 0}
.mission-btn{left:519px;top:1645px;width:179px;height:49px;line-height:49px;font-size:15px}

/* programs */
.programs-title{left:0;top:1884px;width:1200px;text-align:center}
.programs-rule{left:578px;top:1930px}
.program{top:1964px;width:305px;text-align:center}
.program.featured{box-shadow:0 4px 14px rgba(0,0,0,.12);height:413px}
.program-photo{width:305px;height:208px}
.program h3{font-size:15.5px;font-weight:700;line-height:21px;margin-top:32px;color:#222}
.program p{font-size:11px;line-height:17px;color:var(--muted);margin-top:9px}
.program .btn-yellow{margin-top:14px;width:135px;height:39px;line-height:39px;font-size:11.5px}

/* community */
.community{left:0;top:2417px;width:1200px;height:574px;clip-path:polygon(0 38px,100% 0,100% 100%,0 548px);
  background:linear-gradient(90deg,#6b4630 0%,#9a6a48 30%,#a86a2c 45%,#2f7a2a 60%,var(--green) 75%,#0a7a2c 100%)}
.community-title{left:663px;top:2578px;color:var(--white)}
.community-rule{left:665px;top:2624px;background:var(--yellow)}
.community-text{left:663px;top:2642px;width:440px;color:var(--white);font-size:13.2px;line-height:25px}
.community-btn{left:667px;top:2798px;width:156px;height:40px;line-height:40px;font-size:13px}

/* news */
.news-title{left:125px;top:3010px}
.news-rule{left:127px;top:3054px}
.news-card{left:118px;top:3077px;width:480px;height:431px;box-shadow:0 2px 8px rgba(0,0,0,.1)}
.news-hero{width:480px;height:277px;background:linear-gradient(135deg,#e8336a 0%,#f0b32a 35%,#2aa5d8 65%,#8b3bb8 100%)}
.date{display:inline-block;background:var(--green);color:var(--white);font-weight:700;font-size:11px;padding:0 12px;line-height:22px}
.news-card .date{position:absolute;left:6px;top:252px;padding:0 14px;line-height:25px;font-size:13px}
.news-card h3{margin:24px 0 0 24px;font-size:14.5px;font-weight:700}
.news-card p{margin:10px 24px 0;font-size:11px;line-height:20px;color:var(--muted)}
.more{font-weight:700;color:var(--red);text-decoration:underline;text-transform:uppercase}
.news-card .more{display:block;margin:6px 24px 0;font-size:11.5px}
.news-item{left:616px;width:480px;height:129px}
.news-thumb{width:203px;height:129px}
.news-body{left:228px;top:13px;width:250px}
.news-body .date{font-size:9.5px;line-height:18px;padding:0 10px}
.news-body h4{font-size:11.5px;font-weight:700;margin-top:11px}
.news-body p{font-size:9.6px;line-height:17px;color:var(--muted);margin-top:6px}
.news-body .more{display:block;font-size:8.5px;margin-top:4px}

/* support */
.support{left:0;top:3555px;width:1200px;height:588px;clip-path:polygon(0 0,100% 58px,100% 553px,0 100%);
  background:linear-gradient(100deg,#b9141c 0%,#d6421a 35%,#e7811a 65%,var(--gold) 100%)}
.support-title{left:114px;top:3704px;color:var(--white)}
.support-rule{left:116px;top:3749px;background:var(--white)}
.support-text{left:114px;top:3776px;width:440px;color:var(--white);font-size:14px;line-height:26px}
.support-text p+p{margin-top:18px}
.support-btn{left:110px;top:3948px;width:155px;height:46px;line-height:46px;font-size:13px}
.support-photo{left:600px;top:3622px;width:432px;height:432px;border-radius:50%;border:12px solid var(--yellow);
  background:radial-gradient(circle at 50% 55%,#e7d8b8 0%,#c9a978 40%,#5b6fa0 75%,#3a3f5e 100%)}

/* footer */
.footer-brand{left:140px;top:4250px;width:140px;text-align:center;font-weight:700;font-size:20px;color:var(--deep-red)}
.footer-brand .brand-dot{margin:0 auto 10px;width:70px;height:70px}
.social{left:168px;top:4366px;display:flex;gap:8px}
.social span{width:26px;height:26px;border-radius:50%;background:var(--red)}
.footer-col{top:4212px;width:160px}
.footer-col h5{font-size:14.5px;font-weight:700;color:var(--red);padding-bottom:8px;border-bottom:1px solid #ddd}
.footer-col ul{list-style:none;margin-top:14px}
.footer-col li{font-size:11px;color:#555;line-height:27px}
.contact{width:260px}
.contact h5{width:160px}
.contact-row{display:flex;gap:12px;margin-top:14px;font-size:13px;color:#444}
.contact-row small{display:block;font-size:10px;color:#666;line-height:13px}
.copyright-line{left:0;top:4458px;width:1200px;height:1px;background:#ddd}
.copyright{left:0;top:4481px;width:1200px;text-align:center;font-size:11px;color:#777}
</style>
</head>
<body>

<header class="abs site-header">
  <div class="abs brand"><span class="brand-dot"></span>Lomi-Seret</div>
  <nav class="abs main-nav">
    <a class="active" href="#">ABOUT US</a><a href="#">THE COMMUNITY</a><a href="#">PROGRAMS</a><a href="#">NEWS</a><a href="#">ADVOCACY</a><a href="#">PARTNERS</a><a href="#">CONTACT US</a>
  </nav>
</header>

<section class="abs hero" role="img" aria-label="Photo of a crowd of people clapping and celebrating together"></section>
<svg class="abs hero-arrow" style="left:18px" viewBox="0 0 24 40"><path d="M20 4 4 20l16 16" fill="none" stroke="#fff" stroke-width="4"/></svg>
<svg class="abs hero-arrow" style="left:1158px" viewBox="0 0 24 40"><path d="M4 4l16 16L4 36" fill="none" stroke="#fff" stroke-width="4"/></svg>
<div class="abs hero-card">
  <h1>LOMI SERET</h1>
  <p>ETHIOPIA TO ISRAEL AND THE TRANSITION</p>
  <a class="btn btn-red" href="#">Learn more</a>
</div>

<section>
  <div class="abs about-frame"></div>
  <div class="abs about-photo" role="img" aria-label="Photo of three smiling young women"></div>
  <div class="abs eyebrow about-eyebrow">WHO WE ARE</div>
  <h2 class="abs section-title about-title">ABOUT <b>SERET</b></h2>
  <div class="abs rule about-rule"></div>
  <p class="abs about-text">Aliyah (immigration) from Ethiopia to Israel and the transition to a sedentary lifestyle has resulted in the emergence of chronic diseases, in particular diabetes. While only 0.4% of the new immigrants were diagnosed with Type 2 diabetes upon arrival, by the time they had lived in Israel for ten years the figure had risen to 18% - three times as many as in the general population.</p>
  <a class="abs btn btn-green about-btn" href="#">LEARN MORE</a>
</section>

<section>
  <div class="abs mission" role="img" aria-label="Photo of woven red Ethiopian baskets"></div>
  <div class="abs eyebrow mission-eyebrow">WHY WE ARE</div>
  <h2 class="abs section-title mission-title" style="color:#fff">OUR <b>MISSION</b></h2>
  <div class="abs rule mission-rule"></div>
  <p class="abs mission-text">Lorem ipsum dolor sit amet, consectetur adipiscing elit, sed do eiusmod tempor incididunt ut labore et dolore magna aliqua. Ut enim ad minim veniam, quis nostrud exercitation ullamco laboris nisi ut aliquip ex ea commo</p>
  <a class="abs btn btn-yellow mission-btn" href="#">LEARN MORE</a>
</section>

<section>
  <h2 class="abs section-title programs-title">OUR <b>PROGRAMS</b></h2>
  <div class="abs rule programs-rule"></div>
  <article class="abs program" style="left:133px">
    <div class="program-photo" role="img" aria-label="Photo of an audience at a health presentation" style="background:linear-gradient(135deg,#4a3a30,#a08a70 60%,#d8d0c0)"></div>
    <h3>HEALTH &amp; EDUCATION<br>PRESENTATIONS</h3>
    <p>Lorem ipsum dolor sit amet, consectetur<br>adipiscing elit, sed do eiusmod</p>
    <a class="btn btn-yellow" href="#">LEARN MORE</a>
  </article>
  <article class="abs program featured" style="left:451px">
    <div class="program-photo" role="img" aria-label="Photo of a health check at a regional health fair" style="background:linear-gradient(135deg,#6a6a68,#d8d6d0 55%,#8a7a6a)"></div>
    <h3>REGIONAL<br>HEALTH FAIRS</h3>
    <p>Lorem ipsum dolor sit amet, consectetur<br>adipiscing elit, sed do eiusmod</p>
    <a class="btn btn-yellow" href="#">LEARN MORE</a>
  </article>
  <article class="abs program" style="left:772px">
    <div class="program-photo" role="img" aria-label="Photo of a radio host in a studio" style="background:linear-gradient(135deg,#3a3a40,#9a9aa0 55%,#e0e0e4)"></div>
    <h3>AMHARIC RADIO<br>PROGRAM</h3>
    <p>Lorem ipsum dolor sit amet, consectetur<br>adipiscing elit, sed do eiusmod</p>
    <a class="btn btn-yellow" href="#">LEARN MORE</a>
  </article>
</section>

<section>
  <div class="abs community" role="img" aria-label="Photo of many hands joined together, blending into green"></div>
  <h2 class="abs section-title community-title">OUR <b>COMMUNITY</b></h2>
  <div class="abs rule community-rule"></div>
  <p class="abs community-text">Aliyah (immigration) from Ethiopia to Israel and the transition to a sedentary lifestyle has resulted in the emergence of chronic diseases, in particular diabetes. While only 0.4% of the new immigrants were diagnosed with Type 2 diabetes upon arrival, by the time they had lived in Israel for ten years</p>
  <a class="abs btn btn-yellow community-btn" href="#">LEARN MORE</a>
</section>

<section>
  <h2 class="abs section-title news-title">LATEST <b>NEWS</b></h2>
  <div class="abs rule news-rule"></div>
  <article class="abs news-card">
    <div class="news-hero" role="img" aria-label="Photo of colourful woven basket lids"></div>
    <span class="date">28 MAY 2021</span>
    <h3>SED UT PERSPICIATIS UNDE OMNIS ISTE NATUS ERRO</h3>
    <p>Lorem ipsum dolor sit amet, consectetur adipiscing elit, sed do eius-<br>mod tempor incididunt ut labore et dolore magna aliqua.</p>
    <a class="more" href="#">Learn more</a>
  </article>
  <article class="abs news-item" style="top:3077px">
    <div class="news-thumb" role="img" aria-label="Photo of a traditional religious painting" style="background:linear-gradient(135deg,#5a2a1a,#c0702a 50%,#3a4a6a)"></div>
    <div class="abs news-body"><span class="date">28 MAY 2021</span><h4>LOREM IPSUM DOLOR SIT</h4><p>Duis aute irure dolor in reprehenderit in voluptate velit esse cillum dolore</p><a class="more" href="#">Learn more</a></div>
  </article>
  <article class="abs news-item" style="top:3227px">
    <div class="news-thumb" role="img" aria-label="Photo of joined hands" style="background:linear-gradient(135deg,#2a1a14,#8a5a40 55%,#4a3028)"></div>
    <div class="abs news-body"><span class="date">28 MAY 2021</span><h4>LOREM IPSUM DOLOR SIT</h4><p>Duis aute irure dolor in reprehenderit in voluptate velit esse cillum dolore</p><a class="more" href="#">Learn more</a></div>
  </article>
  <article class="abs news-item" style="top:3376px">
    <div class="news-thumb" role="img" aria-label="Photo of colourful woven baskets" style="background:linear-gradient(135deg,#c8a070,#e0306a 45%,#3a9ad0)"></div>
    <div class="abs news-body"><span class="date">28 MAY 2021</span><h4>LOREM IPSUM DOLOR SIT</h4><p>Duis aute irure dolor in reprehenderit in voluptate velit esse cillum dolore</p><a class="more" href="#">Learn more</a></div>
  </article>
</section>

<section>
  <div class="abs support"></div>
  <h2 class="abs section-title support-title">SUPPORT <b>US</b></h2>
  <div class="abs rule support-rule"></div>
  <div class="abs support-text">
    <p>Lomi Seret non-profit organization operates to promote the ethiopian israel community healthcare, using donations and govermant funding.</p>
    <p>Lomi Seret has public institue donation approval (Income Tax instruction, section 46).</p>
  </div>
  <a class="abs btn btn-green support-btn" href="#">LEARN MORE</a>
  <div class="abs support-photo" role="img" aria-label="Photo of community members sharing a meal in a classroom"></div>
</section>

<footer>
  <div class="abs footer-brand"><div class="brand-dot"></div>Lomi-Seret</div>
  <div class="abs social"><span></span><span></span><span></span></div>
  <div class="abs footer-col" style="left:372px">
    <h5>NAVIGATION</h5>
    <ul><li>About Us</li><li>The Community</li><li>Programs</li><li>News</li><li>Partners</li></ul>
  </div>
  <div class="abs footer-col" style="left:607px">
    <h5>RESOURCES</h5>
    <ul><li>Advocacy</li><li>Support Us</li><li>Contact Us</li><li>Privacy Policy</li></ul>
  </div>
  <div class="abs footer-col contact" style="left:809px">
    <h5>CONTACT US</h5>
    <div class="contact-row"><svg width="16" height="16" viewBox="0 0 24 24"><path d="M6.6 10.8a15 15 0 0 0 6.6 6.6l2.2-2.2c.3-.3.7-.4 1-.2 1.1.4 2.3.6 3.6.6.6 0 1 .4 1 1V20c0 .6-.4 1-1 1A17 17 0 0 1 3 4c0-.6.4-1 1-1h3.5c.6 0 1 .4 1 1 0 1.3.2 2.5.6 3.6.1.3 0 .7-.2 1z" fill="#0b6a48"/></svg><div><small>Phone</small>04-5550192</div></div>
    <div class="contact-row"><svg width="16" height="18" viewBox="0 0 24 24"><path d="M12 2a7 7 0 0 0-7 7c0 5 7 13 7 13s7-8 7-13a7 7 0 0 0-7-7zm0 9.5a2.5 2.5 0 1 1 0-5 2.5 2.5 0 0 1 0 5z" fill="#0b6a48"/></svg><div style="font-size:11px"><small>Office</small>Narkis 12/4 POB 1042 Afula, 18110</div></div>
    <div class="contact-row"><svg width="18" height="14" viewBox="0 0 24 18"><path d="M0 0h24v18H0z" fill="#b3141c"/><path d="M0 0l12 9 12-9" fill="none" stroke="#fff" stroke-width="2"/></svg><div style="font-size:11px"><small>Email</small>lomiseret@example.org</div></div>
  </div>
  <div class="abs copyright-line"></div>
  <div class="abs copyright">Copyright © 2022 Lomi Seret</div>
</footer>

</body>
</html>
```